Need Letterhead Design & Matching Business Card

I have a logo that I love already. But the letterhead is less than appealing and boring. I'd like a design for my letterhead which I will match with business cards. Also, I'd like to have used fonts that are generally available, as my current letterhead uses a font named "SPACE" which nobody has unless they download it...so when a Word version is forwarded, it looks awful on the receiver's screed due to not having the font. That being said, modern is the look we like and are going for.

My business is "Halloran Brightmoor PC" - a law firm specializing in representing people who have suffered catastrophic injuries or death (plane, auto, train crashes etc.).

See attached letterhead, which has all of the pertinent information. My logo is also attached in various formats.

```html
<!DOCTYPE html>
<html lang="en">
<head>
<meta charset="utf-8">
<title>Halloran Brightmoor PC — Letterhead &amp; Business Card</title>
<link href="https://fonts.googleapis.com/css2?family=Open+Sans:wght@300;400;600&display=swap" rel="stylesheet">
<style>
  :root {
    --backdrop: #e4e6e8;
    --paper: #fbfbfa;
    --ink: #2b2b2b;
    --ink-soft: #6f6f6f;
    --ink-faint: #9a9a9a;
    --rule: #c9c9c9;
    --brand-dark: #2f2f2f;
    --card-dark: #3b3b3b;
    --on-dark: #f2f2f2;
    --signature-tone: #d9d9d9;
  }
  * { margin: 0; padding: 0; box-sizing: border-box; }
  html, body {
    width: 1200px; height: 800px; overflow: hidden;
    background: var(--backdrop);
    font-family: "Open Sans", Arial, sans-serif;
    color: var(--ink);
  }
  .stage { position: relative; width: 1200px; height: 800px; }

  /* Letterhead */
  .letterhead {
    position: absolute; left: 150px; top: 40px;
    width: 510px; height: 720px;
    background: var(--paper);
    box-shadow: 0 10px 30px rgba(0,0,0,.12);
  }
  .brand-block {
    position: absolute; left: 0; top: 70px;
    width: 118px; height: 118px;
    background: var(--brand-dark);
    display: flex; align-items: center; justify-content: center;
    padding: 10px;
  }
  .brand-name {
    color: var(--on-dark); font-weight: 300; font-size: 11px;
    letter-spacing: .12em; text-transform: uppercase; text-align: center; line-height: 1.6;
  }
  .letter-body {
    position: absolute; left: 88px; top: 200px; width: 350px;
    font-size: 8.4px; line-height: 1.5; color: var(--ink-soft); font-weight: 400;
  }
  .letter-body p { margin-bottom: 9px; }
  .letter-body p:last-child { margin-bottom: 0; }
  .salutation { margin-bottom: 2px !important; }

  .signoff { position: absolute; left: 195px; top: 560px; }
  .signature {
    display: block; width: 120px; height: 22px;
    background: var(--signature-tone); border-radius: 3px; margin-bottom: 6px;
  }
  .signer-name { font-size: 10px; letter-spacing: .04em; color: var(--ink); line-height: 1.4; }
  .signer-title { font-size: 9px; color: var(--ink-faint); font-weight: 300; line-height: 1.4; }

  .letter-footer {
    position: absolute; left: 40px; right: 40px; bottom: 40px;
    border-top: 1px solid var(--rule); padding-top: 14px;
    display: flex; justify-content: space-between;
  }
  .contact-item .label { font-size: 8px; color: var(--ink-soft); display: block; margin-bottom: 3px; }
  .contact-item .value { font-size: 10px; color: var(--ink); }

  /* Business card */
  .business-card {
    position: absolute; left: 740px; top: 300px;
    width: 340px; height: 196px;
    background: var(--card-dark);
    box-shadow: 0 8px 22px rgba(0,0,0,.18);
    display: flex; align-items: center; padding: 0 28px;
    color: var(--on-dark);
  }
  .card-brand {
    flex: 1; font-weight: 300; font-size: 12px; letter-spacing: .12em;
    text-transform: uppercase; line-height: 1.6;
  }
  .card-contact { font-size: 9px; line-height: 1.7; font-weight: 400; }
</style>
</head>
<body>
<main class="stage">

  <section class="letterhead" aria-label="Letterhead">
    <div class="brand-block"><span class="brand-name">Halloran<br>Brightmoor PC</span></div>

    <div class="letter-body">
      <p class="salutation">Dear X,</p>
      <p>Lorem ipsum dolor sit amet, consectetur adipisicing elit, sed do eiusmod tempor incididunt ut labore et dolore magna aliqua. Ut enim ad minim veniam, quis nostrud exercitation ullamco laboris nisi ut aliquip ex ea commodo consequat. Duis aute irure dolor in reprehenderit in voluptate velit esse cillum dolore eu fugiat nulla pariatur. Excepteur sint occaecat cupidatat non proident, sunt in culpa qui officia deserunt mollit anim id est laborum. Sed ut perspiciatis unde omnis iste natus error sit voluptatem accusantium doloremque laudantium, totam rem aperiam, eaque ipsa quae ab illo inventore veritatis et quasi architecto beatae vitae dicta sunt explicabo. Nemo enim ipsam voluptatem quia voluptas sit aspernatur aut odit aut fugit, sed quia consequuntur magni dolores eos qui ratione voluptatem sequi nesciunt. Neque porro voluptatem sequi nesciunt. Nemo enim ipsam voluptatem quia voluptas.</p>
      <p>Lorem ipsum dolor sit amet, consectetur adipisicing elit, sed do eiusmod tempor incididunt ut labore et dolore magna aliqua. Ut enim ad minim veniam, quis nostrud exercitation ullamco laboris nisi ut aliquip ex ea commodo consequat. Duis aute irure dolor in reprehenderit in voluptate velit esse cillum dolore eu fugiat nulla pariatur. Excepteur sint occaecat cupidatat non proident, sunt in culpa qui officia deserunt mollit anim id est laborum. Sed ut perspiciatis unde omnis iste natus error sit voluptatem accusantium doloremque laudantium, totam rem aperiam, eaque ipsa quae ab illo inventore veritatis et quasi architecto beatae vitae dicta sunt explicabo. Nemo enim ipsam voluptatem quia voluptas sit aspernatur aut odit aut.</p>
      <p>Lorem ipsum dolor sit amet, consectetur adipisicing elit, sed do eiusmod tempor incididunt ut labore et dolore magna aliqua. Ut enim ad minim veniam, quis nostrud exercitation ullamco laboris nisi ut aliquip ex ea commodo consequat.</p>
    </div>

    <div class="signoff">
      <span class="signature" role="img" aria-label="Handwritten signature"></span>
      <div class="signer-name">NAME SURNAME</div>
      <div class="signer-title">General Manager</div>
    </div>

    <footer class="letter-footer">
      <div class="contact-item"><span class="label">Phone :</span><span class="value">(03) 9470 5512</span></div>
      <div class="contact-item"><span class="label">Email :</span><span class="value">info@hbpclaw.com</span></div>
      <div class="contact-item"><span class="label">Address :</span><span class="value">PO Box 418, Eastwood Park VIC 8100</span></div>
    </footer>
  </section>

  <section class="business-card" aria-label="Business card">
    <div class="card-brand">Halloran<br>Brightmoor PC</div>
    <div class="card-contact">
      <div>(11) 4455 6677</div>
      <div>info@hbpclaw.com</div>
      <div>Eastwood Park VIC 8100</div>
    </div>
  </section>

</main>
</body>
</html>
```